Business Card Design Project

- makeup artist business card

- original and creative

- Elegant design

- Feel free to come out with cool designs but stick to being elegant and attractive

- Design relates to makeup

- includes name, occupation, contact numbers, email, website

- regular size business card

- round corner card

- double sided

- on 1 side it should just have the website name in the center " velvetbrushhue.com "

Industry/Entity Type

Business

Requirements
Must have
• Marla Tobin
Makeup Artist
USA: +1 (213)555-0147
Singapore: +65 90007312
marlatobin@velvetbrushhue.com
www.velvetbrushhue.com
Should not have
• nothing cartoon looking.
Pictures of makeup being grab from the internet.. Examples: eyes or lips.

```html
<!DOCTYPE html>
<html lang="en">
<head>
<meta charset="utf-8">
<title>Marla Tobin – Makeup Artist Business Card</title>
<link href="https://fonts.googleapis.com/css2?family=Cinzel:wght@400;500&display=swap" rel="stylesheet">
<style>
  :root {
    --backdrop: #e4e6e8;
    --card-black: #0c0b0c;
    --band-grey: #1d1c1e;
    --orange: #f8a51c;
    --coral: #f2706a;
    --magenta: #e8177f;
    --violet: #8c3a9e;
    --gold: #9a7646;
    --white: #ffffff;
    --pink-text: #ec2a8c;
  }
  * { margin: 0; padding: 0; box-sizing: border-box; }
  html, body {
    width: 1067px; height: 1200px; overflow: hidden;
    background: var(--backdrop);
  }
  .canvas { position: relative; width: 1067px; height: 1200px; }

  .card {
    position: absolute;
    width: 420px; height: 560px;
    border-radius: 30px;
    overflow: hidden;
    background: var(--card-black);
    box-shadow: 0 10px 28px rgba(0,0,0,.22);
  }
  .card--front { left: 150px; top: 30px; }
  .card--back  { left: 497px; top: 610px; }

  .card__art { position: absolute; inset: 0; width: 100%; height: 100%; }

  .ornament {
    position: absolute;
    width: 120px; height: 190px;
    background: radial-gradient(ellipse at 50% 60%, rgba(154,118,70,.55), rgba(154,118,70,0) 70%);
  }
  .ornament--left  { left: 0; bottom: 0; }
  .ornament--right { right: 0; bottom: 0; }

  .identity {
    position: absolute;
    left: 95px; right: 15px; top: 284px;
    text-align: center;
    font-family: "Cinzel", serif;
    color: var(--white);
    text-transform: uppercase;
    white-space: nowrap;
  }
  .identity__name { font-size: 36px; font-weight: 400; letter-spacing: -0.5px; line-height: 1; }
  .identity__role { font-size: 9px; letter-spacing: 1px; margin-top: 6px; opacity: .85; }
  .identity__rule {
    height: 3px; width: 180px; margin: 8px auto 22px;
    background: linear-gradient(90deg, rgba(232,23,127,0), var(--magenta) 50%, rgba(232,23,127,0));
  }
  .contact { list-style: none; font-size: 13px; line-height: 1.75; }
  .contact__item--accent { color: var(--pink-text); }

  .domain {
    position: absolute;
    left: 26px; top: 236px;
    font-family: "Cinzel", serif;
    font-size: 25px;
    color: var(--white);
    text-transform: uppercase;
    transform: rotate(-9deg);
    transform-origin: left bottom;
    white-space: nowrap;
  }
</style>
</head>
<body>
<main class="canvas">

  <section class="card card--front" aria-label="Business card front">
    <svg class="card__art" viewBox="0 0 420 560" preserveAspectRatio="none">
      <defs>
        <linearGradient id="front-glow" x1="1" y1="0" x2="0" y2="1">
          <stop offset="0" stop-color="var(--orange)"/>
          <stop offset=".5" stop-color="var(--coral)"/>
          <stop offset="1" stop-color="var(--magenta)"/>
        </linearGradient>
        <radialGradient id="front-shadow" cx=".55" cy=".45" r=".4">
          <stop offset="0" stop-color="var(--violet)" stop-opacity=".55"/>
          <stop offset="1" stop-color="var(--violet)" stop-opacity="0"/>
        </radialGradient>
      </defs>
      <g role="img" aria-label="Close-up photograph of glittering purple eye makeup">
        <path d="M0 0 H420 V245 Q220 255 0 295 Z" fill="url(#front-glow)"/>
        <path d="M0 0 H420 V245 Q220 255 0 295 Z" fill="url(#front-shadow)"/>
      </g>
      <path d="M0 295 Q220 255 420 245 V290 Q240 300 0 330 Z" fill="var(--band-grey)"/>
    </svg>
    <div class="ornament ornament--left" role="img" aria-label="Gold floral swirl ornament"></div>
    <div class="ornament ornament--right" role="img" aria-label="Gold floral swirl ornament"></div>

    <div class="identity">
      <h1 class="identity__name">Marla Tobin</h1>
      <p class="identity__role">Makeup Artist</p>
      <div class="identity__rule"></div>
      <ul class="contact">
        <li class="contact__item">Phone USA: +1 (213)555-0147</li>
        <li class="contact__item">Phone Singapore: +65 90007312</li>
        <li class="contact__item contact__item--accent">marlatobin@velvetbrushhue.com</li>
        <li class="contact__item contact__item--accent">www.velvetbrushhue.com</li>
      </ul>
    </div>
  </section>

  <section class="card card--back" aria-label="Business card back">
    <svg class="card__art" viewBox="0 0 420 560" preserveAspectRatio="none">
      <defs>
        <linearGradient id="back-glow" x1="1" y1="0" x2="0" y2="1">
          <stop offset="0" stop-color="var(--orange)"/>
          <stop offset=".5" stop-color="var(--coral)"/>
          <stop offset="1" stop-color="var(--magenta)"/>
        </linearGradient>
        <radialGradient id="back-shadow" cx=".6" cy=".4" r=".4">
          <stop offset="0" stop-color="var(--violet)" stop-opacity=".55"/>
          <stop offset="1" stop-color="var(--violet)" stop-opacity="0"/>
        </radialGradient>
      </defs>
      <g role="img" aria-label="Close-up photograph of glittering purple eye makeup">
        <path d="M0 0 H420 V170 Q220 200 0 290 Z" fill="url(#back-glow)"/>
        <path d="M0 0 H420 V170 Q220 200 0 290 Z" fill="url(#back-shadow)"/>
      </g>
      <path d="M0 290 Q220 200 420 170 V230 Q230 250 0 330 Z" fill="var(--band-grey)"/>
    </svg>
    <div class="ornament ornament--left" role="img" aria-label="Gold floral swirl ornament"></div>
    <div class="ornament ornament--right" role="img" aria-label="Gold floral swirl ornament"></div>
    <p class="domain">www.velvetbrushhue.com</p>
  </section>

</main>
</body>
</html>
```